Midnight Lantern Diva

We have started working on a website for our short film. The goals of this website are:
• Attract talent, financiers + distributors to the feature film.
• Start e-commerce business to generate buzz for the film.

Who is our target audience?
• Kung Fu fans.
• Guitar players.
• Women filmmakers.
• Chinese film fans.

Information we want on this website.
Web 1.0 Components
• Media - trailer and stills

We are looking to include the following pages:
1. Home page
2. About
3. Photos
4. Cast & Crew
5. News
6. Media (reviews)
7. Store
8. Contact

Web 2.0 Components
• Mailing list sign-up
• Blog - with comments section
• Like / Add buttons - to all social networks
• Feeds - from social media
• Links - social media
• Widgets - that anyone can put on their sites

Attached is a mock up of the landing page (possible T-shirt) we are developing plus photos we would like on the website.

Thank you.
Updates

Reason: I am at a film market in meetings for my film project. Next week will be used for script rewrites. After that I will choose a design.

Hello Folks,

I have added my company logo to my brief. My answer is yes - I would like that added to the website.
Thanks!
M-

Reason: I have added more photos and included two (in front of a white screen) that can easily be photoshopped into a great landing page. M-

I have added more photos. Also I have two photos taken in front of a white screen that can easily be photo-shopped into a cool landing page. I have also gotten rid of the "crowd" photo in my mock up of the design I am looking for. 

I've extended the deadline by 2 days.

M-

Target Market(s)

• Kung Fu fans.
• Guitar players.
• Women filmmakers.
• Chinese film fans.

Industry/Entity Type

E-Commerce

Colors
ec2027

Requirements
Must have
• Trailer, movie stills, links to social media.
Nice to have
• All of the above

```html
<!DOCTYPE html>
<html lang="en">
<head>
<meta charset="utf-8">
<title>Midnight Lantern Diva</title>
<link rel="stylesheet" href="https://fonts.googleapis.com/css2?family=Oswald:wght@500;700&family=Open+Sans:wght@300;400&display=swap">
<style>
  :root {
    --page-dark: #161616;
    --panel: #000000;
    --frame: #d9d9d9;
    --red: #a8100f;
    --red-text: #b81818;
    --gold-top: #ffd51a;
    --gold-bottom: #e79a12;
    --white: #ffffff;
    --input-grey: #c8c8c8;
  }
  * { box-sizing: border-box; margin: 0; padding: 0; }
  html, body { width: 1200px; height: 900px; overflow: hidden; background: var(--page-dark); }
  .canvas { position: relative; width: 1200px; height: 900px; overflow: hidden; }

  .stage-backdrop {
    position: absolute; inset: 0;
    background:
      radial-gradient(ellipse 320px 220px at 120px 170px, rgba(200,200,200,.55), transparent 70%),
      radial-gradient(ellipse 300px 240px at 1080px 150px, rgba(210,210,210,.6), transparent 70%),
      radial-gradient(ellipse 700px 200px at 600px 360px, rgba(120,120,120,.45), transparent 75%),
      linear-gradient(180deg, #3a3a3a 0%, #5a5a5a 30%, #2a2a2a 55%, #151515 80%, #111 100%);
  }
  .top-bar { position: absolute; left: 0; top: 0; width: 1200px; height: 10px; background: #1c1c1c; }

  .sidebar { position: absolute; left: 196px; top: 38px; width: 220px; }
  .brand {
    height: 118px; background: var(--panel); border: 1px solid var(--frame);
    display: flex; align-items: center; justify-content: center; text-align: center;
    font-family: "Oswald", sans-serif; font-weight: 500; color: var(--white);
    font-size: 27px; line-height: 1.05; text-transform: uppercase; padding: 0 18px;
  }
  .nav { list-style: none; margin-top: 8px; }
  .nav li { height: 50px; margin-bottom: 6.5px; }
  .nav a {
    display: flex; height: 100%; align-items: center; justify-content: center;
    background: var(--panel); border: 1px solid var(--frame);
    font-family: "Oswald", sans-serif; font-weight: 500; font-size: 24px;
    color: var(--red-text); text-decoration: none; text-transform: uppercase;
  }
  .nav a.is-current { background: var(--red); color: #000; }
  .social { display: flex; gap: 7px; margin-top: 4px; }
  .social a {
    width: 50px; height: 50px; display: flex; align-items: center; justify-content: center;
    background: linear-gradient(var(--gold-top), var(--gold-bottom));
    border: 1px solid #fff3a0; color: #000; text-decoration: none;
    font-family: "Oswald", sans-serif; font-weight: 500; font-size: 13px;
  }

  .content-panel {
    position: absolute; left: 429px; top: 38px; width: 529px; height: 845px;
    background: var(--panel); border: 1px solid var(--frame);
  }
  .hero {
    position: absolute; left: 8px; top: 8px; width: 511px; height: 415px;
    background:
      radial-gradient(ellipse 220px 150px at 140px 90px, rgba(255,255,255,.95), transparent 70%),
      radial-gradient(ellipse 220px 160px at 420px 110px, rgba(255,255,255,.9), transparent 70%),
      linear-gradient(180deg, #f2b7b3 0%, #e0242a 45%, #7a0d10 65%, #120202 85%, #000 100%);
  }
  .headline {
    position: absolute; left: 0; width: 100%; top: 428px; text-align: center;
    font-family: "Oswald", sans-serif; font-weight: 700; font-size: 44px; line-height: 1.2;
    text-transform: uppercase; letter-spacing: -0.5px;
    background: linear-gradient(var(--gold-top), var(--gold-bottom));
    -webkit-background-clip: text; background-clip: text; color: transparent;
  }
  .divider { position: absolute; left: 47px; width: 433px; height: 1px; background: #2a2a2a; }
  .divider.upper { top: 489px; }
  .divider.lower { top: 810px; }

  .welcome-title {
    position: absolute; left: 28px; top: 502px;
    font-family: "Open Sans", sans-serif; font-weight: 300; font-size: 27px; color: var(--red-text);
  }
  .welcome-photo {
    position: absolute; left: 324px; top: 511px; width: 169px; height: 102px;
    background: linear-gradient(135deg, #9b1e22 0%, #c8464a 40%, #5a2a24 75%, #2a1a18 100%);
    border: 1px solid #333;
  }
  .welcome-copy {
    position: absolute; left: 30px; top: 547px; width: 460px;
    font-family: "Open Sans", sans-serif; font-size: 10.5px; line-height: 13px; color: var(--white);
    white-space: nowrap;
  }
  .welcome-copy p { margin-bottom: 13px; }
  .welcome-copy a { color: var(--red-text); text-decoration: none; }

  .newsletter {
    position: absolute; left: 27px; top: 729px; width: 472px; height: 70px;
    border: 1px solid var(--frame);
  }
  .newsletter h2 {
    position: absolute; left: 0; width: 100%; top: 2px; text-align: center;
    font-family: "Oswald", sans-serif; font-weight: 700; font-size: 26px; line-height: 38px;
    text-transform: uppercase; letter-spacing: -0.4px; white-space: nowrap;
    background: linear-gradient(var(--gold-top), var(--gold-bottom));
    -webkit-background-clip: text; background-clip: text; color: transparent;
  }
  .newsletter label {
    position: absolute; left: 23px; top: 42px;
    font-family: "Open Sans", sans-serif; font-weight: 300; font-size: 14px; color: #ddd;
  }
  .newsletter .email-field {
    position: absolute; left: 276px; top: 43px; width: 150px; height: 18px;
    background: var(--input-grey); border: 0;
  }
  .newsletter .submit {
    position: absolute; left: 426px; top: 43px; width: 18px; height: 18px;
    background: var(--red); color: #fff; border: 0;
    font-family: "Open Sans", sans-serif; font-size: 12px; line-height: 18px; text-align: center;
  }
  .copyright {
    position: absolute; left: 0; width: 100%; top: 817px; text-align: center;
    font-family: "Open Sans", sans-serif; font-size: 11px; color: var(--white);
  }
</style>
</head>
<body>
<div class="canvas">
  <div class="stage-backdrop" role="img" aria-label="Greyscale concert stage with smoke, lights and a cheering crowd"></div>
  <div class="top-bar"></div>

  <aside class="sidebar">
    <div class="brand">Midnight Lantern Diva</div>
    <ul class="nav">
      <li><a class="is-current" href="#">Home</a></li>
      <li><a href="#">About</a></li>
      <li><a href="#">Photos</a></li>
      <li><a href="#">Cast &amp; Crew</a></li>
      <li><a href="#">News</a></li>
      <li><a href="#">Media</a></li>
      <li><a href="#">Store</a></li>
      <li><a href="#">Contact</a></li>
    </ul>
    <div class="social">
      <a href="#">Chirp</a>
      <a href="#">Pals</a>
      <a href="#">Loop</a>
      <a href="#">Reel</a>
    </div>
  </aside>

  <main class="content-panel">
    <div class="hero" role="img" aria-label="Red-lit concert scene: a martial artist leaps above crossed guitars and a cheering crowd"></div>
    <h1 class="headline">Let’s Rock!</h1>
    <div class="divider upper"></div>

    <h2 class="welcome-title">Welcome</h2>
    <div class="welcome-photo" role="img" aria-label="Film still of two actors in a red-lit scene"></div>
    <div class="welcome-copy">
      <p>We have started working on a website for our short film.<br>The goals of this website are.</p>
      <p>Attract talent, financiers + distributors to the feature film.<br>Start e-commerce business to generate buzz for the film.</p>
      <p>The above text and the following text is just an example to display what text will look like on<br>the page in the content area. With this particular website, we can either build it custom, or<br>utilize an open source application, like PressLeaf. Another idea is to go with a template<br>builder program, like Website Builder through SiteHarbor, and then modify to look like this.</p>
      <p>If you have questions for me, feel free to reach out to me at <a href="#">hello@lanterndiva.example</a>.</p>
    </div>

    <form class="newsletter">
      <h2>Sign up for our rockin’ newsletter!</h2>
      <label for="news-email">Just fill in your e-mail here to get started</label>
      <input class="email-field" id="news-email" type="email">
      <button class="submit" type="button">&gt;</button>
    </form>

    <div class="divider lower"></div>
    <p class="copyright">Copyright © 2014 Midnight Lantern Diva. All rights reserved.</p>
  </main>
</div>
</body>
</html>
```